Adult Job Portal needs a Web Design

We need a web design for a landing and search page for an ADULT-JOB-portal.

The structure of landing page can be taken from zestmingle.com.

The structure of job search page can be taken from: http://www.careersinfenbury.co.uk/

Users should be able to recognize that is a SEX-INDUSTRY job portal.

The project name can not be published for ... some reasons.
Updates

Hi, Hivelings.

Please note: the project was upgraded to "Guaranteed"
Thanks in advance for great work.
BR. M.

Hi ArtHivelings,
please find attached the landing page wireframe.
It should make it easier for you to know what is expected.
Thanks in advance, guys!

Target Market(s)

women 18 to 30 years old

Industry/Entity Type

Adult

Requirements
Must have
• We expect to get design for the following pages:
- Landing page
- Add profile (name, description, photos, skills, preferable location)
- Job search with filters (example http://www.careersinfenbury.co.uk/jobs)
- Companies list (example http://www.careersinfenbury.co.uk/companies-in-fenbury)
- Company page (example http://www.careersinfenbury.co.uk/company/pelvoro)
Should not have
• pornography, violence

```html
<!DOCTYPE html>
<html lang="en">
<head>
<meta charset="utf-8">
<title>Company Name — Find Your Next Job</title>
<link rel="stylesheet" href="https://fonts.googleapis.com/css2?family=Arimo:wght@400;700&family=Montserrat:wght@400;500;600&family=Oswald:wght@400;500;600&family=Podkova:wght@700&display=swap">
<style>
  :root {
    --white: #ffffff;
    --ink: #1c1c1c;
    --text-grey: #6a6a6a;
    --rule-grey: #e3e3e3;
    --icon-faint: #e9ecef;
    --amber: #fbb01f;
    --amber-deep: #f28d1d;
    --gold-top: #ffc21d;
    --gold-bottom: #e9960a;
    --red-top: #ff2a22;
    --red-bottom: #d80d0d;
    --footer: #2b2b2b;
    --phone-body: #1e1e1e;
  }
  * { box-sizing: border-box; margin: 0; padding: 0; }
  html, body { width: 1200px; height: 1067px; overflow: hidden; background: var(--white); }
  body { position: relative; font-family: "Arimo", Arial, sans-serif; color: var(--ink); }

  .hero { position: absolute; left: 0; top: 0; width: 1200px; height: 581px; overflow: hidden; }
  .hero-photo {
    position: absolute; inset: 0;
    background:
      radial-gradient(ellipse 420px 300px at 380px 300px, #7a5a45 0%, rgba(122,90,69,0) 70%),
      radial-gradient(ellipse 360px 260px at 700px 260px, #8a6a55 0%, rgba(138,106,85,0) 70%),
      linear-gradient(180deg, #a9a4a3 0%, #8d8482 45%, #b8b4b5 100%);
  }
  .brand { position: absolute; left: 132px; top: 30px; font-family: "Montserrat", sans-serif; font-weight: 500; font-size: 35px; letter-spacing: 0.5px; color: var(--white); }
  .audience-nav { position: absolute; top: 25px; left: 836px; display: flex; gap: 4px; }
  .audience-nav a {
    display: block; height: 33px; line-height: 33px; border-radius: 17px;
    font-family: "Montserrat", sans-serif; font-weight: 600; font-size: 14px; color: var(--white); text-decoration: none; text-align: center;
  }
  .audience-nav .for-girls { width: 111px; background: linear-gradient(var(--gold-top), var(--gold-bottom)); }
  .audience-nav .for-clubs { width: 117px; background: linear-gradient(var(--red-top), var(--red-bottom)); }

  .hero-title { position: absolute; left: 128px; top: 156px; font-family: "Podkova", serif; font-weight: 700; font-size: 54px; letter-spacing: 0; color: var(--white); text-shadow: 0 2px 4px rgba(0,0,0,0.35); white-space: nowrap; }
  .hero-intro { position: absolute; left: 132px; top: 238px; width: 590px; font-weight: 700; font-size: 17px; line-height: 26.4px; color: var(--white); text-shadow: 0 1px 2px rgba(0,0,0,0.35); }

  .subscribe { position: absolute; left: 132px; top: 433px; width: 551px; height: 82px; background: rgba(30,24,22,0.72); border-radius: 4px; }
  .subscribe .email { position: absolute; left: 18px; top: 19px; width: 346px; height: 41px; background: var(--white); border-radius: 3px; padding-left: 10px; line-height: 41px; font-family: "Montserrat", sans-serif; font-size: 15px; color: #333; }
  .subscribe .subscribe-btn { position: absolute; left: 380px; top: 19px; width: 150px; height: 43px; border-radius: 3px; background: linear-gradient(var(--gold-top), var(--gold-bottom)); text-align: center; line-height: 43px; font-family: "Oswald", sans-serif; font-weight: 500; font-size: 22px; color: var(--ink); letter-spacing: 0.5px; }

  .phone { position: absolute; left: 761px; top: 134px; width: 265px; height: 506px; z-index: 2; }

  .search-band { position: absolute; left: 0; top: 581px; width: 1200px; height: 197px; background: linear-gradient(180deg, var(--amber) 0%, var(--amber-deep) 100%); }
  .jobs-count { position: absolute; left: 131px; top: 48px; font-family: "Oswald", sans-serif; font-weight: 500; font-size: 30px; color: var(--ink); }
  .jobs-count strong { font-weight: 600; font-size: 44px; margin-right: 6px; }
  .field { position: absolute; top: 123px; height: 37px; background: var(--white); border-radius: 2px; padding-left: 14px; line-height: 37px; font-family: "Montserrat", sans-serif; font-size: 16px; color: #333; }
  .field-what { left: 131px; width: 377px; }
  .field-where { left: 523px; width: 376px; }
  .find-btn { position: absolute; left: 914px; top: 123px; width: 154px; height: 37px; background: linear-gradient(#ffffff, #e6e6e6); border-radius: 2px; display: flex; align-items: center; }
  .find-btn .icon { width: 44px; height: 37px; border-right: 1px solid #cfcfcf; display: flex; align-items: center; justify-content: center; }
  .find-btn span { flex: 1; text-align: center; font-family: "Oswald", sans-serif; font-size: 19px; color: var(--ink); }

  .steps { position: absolute; left: 0; top: 778px; width: 1200px; height: 234px; }
  .step { position: absolute; top: 0; width: 310px; height: 234px; }
  .step .faint-icon { position: absolute; top: 28px; left: 150px; }
  .step h2 { position: absolute; top: 24px; left: 0; font-family: "Oswald", sans-serif; font-weight: 500; font-size: 34px; color: var(--ink); }
  .step p { position: absolute; top: 78px; left: 0; width: 300px; font-family: "Montserrat", sans-serif; font-size: 14px; line-height: 21.6px; color: var(--text-grey); }
  .step-find { left: 132px; }
  .step-apply { left: 455px; }
  .step-move { left: 778px; }
  .divider { position: absolute; top: 30px; width: 1px; height: 165px; background: var(--rule-grey); }
  .divider-first { left: 438px; }
  .divider-second { left: 761px; }

  .site-footer { position: absolute; left: 0; top: 1012px; width: 1200px; height: 55px; background: var(--footer); }
  .site-footer .copyright { position: absolute; left: 132px; top: 19px; font-family: "Montserrat", sans-serif; font-size: 12.5px; color: var(--white); }
  .social { position: absolute; top: 14px; left: 972px; display: flex; gap: 7px; }
  .social span { display: block; width: 27px; height: 27px; border-radius: 50%; background: var(--white); }
</style>
</head>
<body>
  <header class="hero">
    <div class="hero-photo" role="img" aria-label="Soft-focus portrait photograph of a young woman, warm brown and grey tones"></div>
    <div class="brand">COMPANY NAME</div>
    <nav class="audience-nav">
      <a class="for-girls" href="#">FOR GIRLS</a>
      <a class="for-clubs" href="#">FOR CLUBS</a>
    </nav>
    <h1 class="hero-title">FIND YOUR NEXT JOB</h1>
    <p class="hero-intro">This is Pixelforge's version&nbsp; of Lorem Ipsum. Proin gravida nibh vel velit auctor aliquet. Aenean sollicitudin, lorem quis bibendum auctor, nisi elit consequat ipsum, nec sagittis sem nibh id elit. Duis sed odio sit amet nibh vulputate cursus a sit amet mauris. Morbi accumsan ipsum velit. Nam nec tellus a odio tincidunt auctor a ornare odio. Sed non&nbsp; mauris vitae erat consequat auctor eu in elit.</p>
    <form class="subscribe">
      <div class="email">Enter Your Email Address</div>
      <div class="subscribe-btn">SUBSCRIBE</div>
    </form>
  </header>

  <svg class="phone" viewBox="0 0 265 506" role="img" aria-label="Smartphone showing the app start screen with a photo and a Find Your Next Job button">
    <defs>
      <linearGradient id="screen-tone" x1="0" y1="0" x2="0" y2="1">
        <stop offset="0" stop-color="#6b4a3a"/>
        <stop offset="0.5" stop-color="#8a6550"/>
        <stop offset="1" stop-color="#4a3328"/>
      </linearGradient>
    </defs>
    <rect x="0" y="0" width="265" height="506" rx="26" fill="var(--phone-body)"/>
    <rect x="18" y="48" width="229" height="392" fill="url(#screen-tone)"/>
  </svg>

  <section class="search-band">
    <div class="jobs-count"><strong>1762</strong>Jobs Available</div>
    <div class="field field-what">What</div>
    <div class="field field-where">Where in Company name?</div>
    <div class="find-btn">
      <div class="icon">
        <svg width="26" height="26" viewBox="0 0 26 26" aria-hidden="true"><circle cx="15" cy="11" r="8" fill="none" stroke="#1c1c1c" stroke-width="2.4"/><line x1="9.5" y1="16.5" x2="3" y2="23" stroke="#1c1c1c" stroke-width="3.2" stroke-linecap="round"/></svg>
      </div>
      <span>FIND JOB</span>
    </div>
  </section>

  <section class="steps">
    <article class="step step-find">
      <svg class="faint-icon" width="150" height="150" viewBox="0 0 150 150" aria-hidden="true"><circle cx="55" cy="55" r="42" fill="none" stroke="var(--icon-faint)" stroke-width="16"/><line x1="88" y1="88" x2="130" y2="130" stroke="var(--icon-faint)" stroke-width="20" stroke-linecap="round"/></svg>
      <h2>FIND</h2>
      <p>This is Pixelforge's version&nbsp; of Lorem Ipsum. Proin gravida nibh vel velit auctor aliquet. Aenean sollicitudin, lorem quis bibendum auctor, nisi elit consequat ipsum, nec sagittis sem nibh id elit.</p>
    </article>
    <div class="divider divider-first"></div>
    <article class="step step-apply">
      <svg class="faint-icon" width="150" height="150" viewBox="0 0 150 150" aria-hidden="true"><polyline points="15,70 55,115 140,20" fill="none" stroke="var(--icon-faint)" stroke-width="24" stroke-linecap="round" stroke-linejoin="round"/></svg>
      <h2>APPLY</h2>
      <p>This is Pixelforge's version&nbsp; of Lorem Ipsum. Proin gravida nibh vel velit auctor aliquet. Aenean sollicitudin, lorem quis bibendum auctor, nisi elit consequat ipsum, nec sagittis sem nibh id elit.</p>
    </article>
    <div class="divider divider-second"></div>
    <article class="step step-move">
      <svg class="faint-icon" width="150" height="150" viewBox="0 0 150 150" aria-hidden="true"><g fill="var(--icon-faint)"><polygon points="75,0 110,40 88,40 88,150 62,150 62,40 40,40"/><polygon points="20,60 60,90 20,120"/><polygon points="130,60 90,90 130,120"/></g></svg>
      <h2>MOVE</h2>
      <p>This is Pixelforge's version&nbsp; of Lorem Ipsum. Proin gravida nibh vel velit auctor aliquet. Aenean sollicitudin, lorem quis bibendum auctor, nisi elit consequat ipsum, nec sagittis sem nibh id elit.</p>
    </article>
  </section>

  <footer class="site-footer">
    <p class="copyright">Copyright © 2013 Companyname. All Rights Reserved.</p>
    <div class="social" aria-label="Social links"><span></span><span></span><span></span></div>
  </footer>
</body>
</html>
```